lunch and dinne(al a carte) menus

we are a medium sized licenced club that has taken back the dining in the club
in the western suburbs of sydney working class with a rugby league base
our logo is a wolf penbury hawks

Reason: We have changed the name to 77-13 diner it could be done as seventy 13 or 77 thirteen or seventy thirteen We need a lunch menu and a seperate dinner menu eg seventy 13 diner l u n c h or 77 thirteen diner d i n n e r

Reason: Weve changed the name

Target Market(s)

young families, working class rugby leagues sporty types

Industry/Entity Type

Club

Requirements
Must have
• user friendly

```html
<!DOCTYPE html>
<html lang="en">
<head>
<meta charset="utf-8">
<title>Hawks Lunch Menu</title>
<link rel="stylesheet" href="https://fonts.googleapis.com/css2?family=Alfa+Slab+One&family=Alegreya:wght@800;900&display=swap">
<style>
  :root {
    --wood-dark: #3b2414;
    --wood-mid: #6a4226;
    --wood-light: #85563a;
    --felt-dark: #163c22;
    --felt-mid: #24532f;
    --paper-light: #e6c59c;
    --paper-mid: #d9a978;
    --title-cream: #e8d6c0;
    --heading-brown: #7b4a2b;
    --ink: #5a1d0c;
    --footer-text: #efe3d4;
  }
  html, body { margin: 0; padding: 0; overflow: hidden; }
  body { width: 848px; height: 1200px; position: relative; background: var(--felt-dark); }
  .menu { position: absolute; inset: 0; width: 848px; height: 1200px; overflow: hidden; }

  .backdrop {
    position: absolute; left: 0; top: 130px; width: 848px; height: 990px;
    background:
      repeating-linear-gradient(90deg, rgba(0,0,0,.12) 0 2px, transparent 2px 120px),
      linear-gradient(180deg, var(--felt-mid), var(--felt-dark));
  }
  .wood-band {
    position: absolute; left: 0; width: 848px;
    background:
      repeating-linear-gradient(180deg, rgba(0,0,0,.10) 0 3px, transparent 3px 11px),
      linear-gradient(180deg, var(--wood-light), var(--wood-mid) 50%, var(--wood-dark));
    box-shadow: 0 0 14px rgba(0,0,0,.6);
  }
  .wood-band.top { top: 0; height: 130px; }
  .wood-band.bottom { top: 1115px; height: 85px; }

  .menu-title {
    position: absolute; top: 28px; left: 0; width: 848px; margin: 0;
    text-align: center; font-family: "Alfa Slab One", serif; font-weight: 400;
    font-size: 62px; line-height: 70px; letter-spacing: -1.5px; word-spacing: -6px;
    color: var(--title-cream); text-shadow: 2px 3px 3px rgba(0,0,0,.55);
  }

  .parchment {
    position: absolute; left: 84px; top: 130px; width: 682px; height: 905px;
    background: radial-gradient(ellipse at 45% 40%, var(--paper-light), var(--paper-mid));
    box-shadow: 0 4px 16px rgba(0,0,0,.55);
  }

  .section-head {
    position: absolute; left: 136px; top: 164px; margin: 0;
    font-family: "Alfa Slab One", serif; font-weight: 400; font-size: 35px;
    letter-spacing: -.5px; color: var(--heading-brown);
  }
  .col-label {
    position: absolute; top: 184px; font-family: "Alegreya", serif; font-weight: 900;
    font-size: 16px; color: var(--heading-brown); width: 80px; text-align: center;
  }
  .col-label.member { left: 535px; }
  .col-label.visitor { left: 620px; }
  .rule { position: absolute; left: 136px; top: 214px; width: 550px; border-top: 1.5px dashed #8a6048; }

  .dish { position: absolute; left: 138px; width: 560px; color: var(--ink); }
  .dish-name { margin: 0; font-family: "Alegreya", serif; font-weight: 900; font-size: 16px; line-height: 20px; }
  .dish-desc { margin: 0; font-family: "Alegreya", serif; font-weight: 900; font-size: 13.5px; line-height: 17.5px; }
  .price {
    position: absolute; top: 0; width: 50px; text-align: center;
    font-family: "Alegreya", serif; font-weight: 900; font-size: 15px; line-height: 20px;
  }
  .price.member { left: 412px; }
  .price.visitor { left: 497px; }

  .footer-note {
    position: absolute; top: 1147px; left: 0; width: 848px; margin: 0; text-align: center;
    font-family: "Alfa Slab One", serif; font-size: 14.5px; letter-spacing: -.4px; word-spacing: -2px;
    color: var(--footer-text); text-shadow: 1px 1px 2px rgba(0,0,0,.6);
  }
</style>
</head>
<body>
<main class="menu">
  <div class="backdrop"></div>

  <div class="parchment" role="img" aria-label="Aged torn parchment sheet"></div>

  <header class="wood-band top">
    <h1 class="menu-title">HAWKS LUNCH MENU</h1>
  </header>

  <h2 class="section-head">CHARGRILL</h2>
  <div class="col-label member">Member</div>
  <div class="col-label visitor">Visitor</div>
  <div class="rule"></div>

  <article class="dish" style="top:226px">
    <h3 class="dish-name">MAD COW</h3>
    <p class="dish-desc" style="margin-top:2px">A large tender rump topped with bug tail meat<br>calamari, scallops, prawns &amp; mussels.<br>All in a garlic white sauce</p>
    <span class="price member">$28</span><span class="price visitor">$30</span>
  </article>

  <article class="dish" style="top:318px">
    <h3 class="dish-name">BBQ</h3>
    <p class="dish-desc">Massive rump steak cooked the way God intended it,<br>with bacon melted cheddar, onion rings, corn kernals<br>and beetroot finished with a dollop of sour cream</p>
    <span class="price member">$28</span><span class="price visitor">$30</span>
  </article>

  <article class="dish" style="top:407px">
    <h3 class="dish-name">CLUB SPECIAL</h3>
    <p class="dish-desc">Scotch fillet steak cooked with love, topped with fried<br>bacon fanned avocado &amp; melkted camembert cheese<br>with the sauce of your choice</p>
    <span class="price member">$28</span><span class="price visitor">$30</span>
  </article>

  <article class="dish" style="top:496px">
    <h3 class="dish-name">SURF &amp; TURF</h3>
    <p class="dish-desc">Tender scotch fillet steak topped with large tiger<br>prawns in a cream sauce</p>
    <span class="price member">$28</span><span class="price visitor">$30</span>
  </article>

  <article class="dish" style="top:568px">
    <h3 class="dish-name">F100 STEAK</h3>
    <p class="dish-desc">Huge rump steak topped with fanned avocado,<br>melted cheese &amp; button mushroom sauce</p>
    <span class="price member">$28</span><span class="price visitor">$30</span>
  </article>

  <article class="dish" style="top:640px">
    <h3 class="dish-name">THE FULL HOUSE</h3>
    <p class="dish-desc">A massive T-bone steak topped with a special<br>seafood mix of prawns, calamari, mussels, scallops etc<br>with spicy tomato &amp; basil sauce</p>
    <span class="price member">$28</span><span class="price visitor">$30</span>
  </article>

  <article class="dish" style="top:729px">
    <h3 class="dish-name">CATTLEMANS STEAK</h3>
    <p class="dish-desc">350g rib eye steak on the bone</p>
    <span class="price member">$28</span><span class="price visitor">$30</span>
  </article>

  <article class="dish" style="top:784px">
    <h3 class="dish-name">BBQ AMERICAN PORK RIBS</h3>
    <p class="dish-desc">Hickory smoked pork ribs, roasted in a BBQ sauce</p>
    <span class="price member">$28</span><span class="price visitor">$30</span>
  </article>

  <article class="dish" style="top:838px">
    <h3 class="dish-name">RIB COMBO 1</h3>
    <p class="dish-desc">Hickory smoked pork ribs, roasted in a BBQ sauce</p>
    <span class="price member">$28</span><span class="price visitor">$30</span>
  </article>

  <article class="dish" style="top:893px">
    <h3 class="dish-name">RIB COMBO 2</h3>
    <p class="dish-desc">Hickory smoked pork ribs, with char grilled rump steak</p>
    <span class="price member">$28</span><span class="price visitor">$30</span>
  </article>

  <footer class="wood-band bottom"></footer>
  <p class="footer-note">ALL MAIN MEALS ARE SERVED WITH CHIPS &amp; SALAD OR MASHED POTATO &amp; VEGETABLES</p>
</main>
</body>
</html>
```